Looking for a cutting-edge design for a healthy, all-nautural dog treats package

We are launching an All-Natural dog treat. It is made of 5 simple ingredients (peanut butter, sweet potatoes, potato flour, flaxseed oil & eggs). This product is white-labeled (meaning the original manufacturer will be producing them for us under our own name). The brand name is TrailHop.

What We Are Looking For:
We are looking for an approach that really emphasizes the fact that it will be all-natural, grain-free. In fact, we are looking for a design that is very similar to the qu loaf (please take a look at quloafdemo.net for examples).

Other Details to Remember:
Attached is a png file of the dimensions provided by the original manufacturer. Please note that our bag will the a "brown paper bag" color. Finally, the back of the bag should include the same verbiage as the original (although does not have to be the same design/fonts).
Updates

Project Deadline Extended Reason: It appears that the package can now only be in one color on "brown paper bag" of "off white" packaging. Added Wednesday, October 26, 2016

Target Market(s)

Dog owners that appreciate quality food for their pets...more than likely, they are foodies themselves and/or health conscience

Industry/Entity Type

Pet

Logo Text

TrailHop

Requirements
Must have
• Emphasis on the product being all-natural, grain-free. Looks similar to the quloaf packaging (quloafdemo.net)
• **IMPORTANT UPDATE**
• The packaging people have notified us that all graphics or lettering must be in ONE SAME COLOR. The package itself will be in either "brown paper bag" or "off white" color.
Should not have
• That being said, please do NOT make it look absolutely identical to the qu loaf

```html
<!DOCTYPE html>
<html lang="en">
<head>
<meta charset="utf-8">
<title>TrailHop – All-Natural Dog Treats</title>
<link rel="stylesheet" href="https://fonts.googleapis.com/css2?family=Rye&family=Oswald:wght@300;400&display=swap">
<style>
  :root {
    --kraft: #c4905b;
    --label: #f1efeb;
    --ink: #6a2c15;
    --tan: #d6a06d;
    --rule: #9b8a7c;
  }
  * { margin: 0; padding: 0; box-sizing: border-box; }
  html, body { width: 1200px; height: 895px; overflow: hidden; }
  body { background: var(--kraft); position: relative; font-family: "Oswald", sans-serif; }

  .front-label {
    position: absolute;
    left: 365px; top: 105px;
    width: 470px; height: 760px;
    background: var(--label);
  }
  .brand-name {
    position: absolute;
    left: 345px; top: 40px; width: 510px;
    text-align: center;
    font-family: "Rye", serif;
    font-size: 74px;
    line-height: 1;
    color: var(--ink);
    letter-spacing: 1px;
  }
  .hero-art {
    position: absolute;
    left: 95px; top: 60px;
    width: 280px; height: 210px;
    background: radial-gradient(ellipse at center, #e4b688 0%, #ecd2b6 55%, var(--label) 78%);
  }
  .ingredient-list {
    position: absolute;
    left: 36px; top: 285px; width: 398px;
    list-style: none;
    border-top: 1px dotted var(--rule);
  }
  .ingredient-list li {
    display: flex; align-items: center;
    height: 60px;
    border-bottom: 1px dotted var(--rule);
  }
  .tick {
    width: 42px; height: 100%;
    display: flex; align-items: center; justify-content: center;
    border-right: 1px solid var(--rule);
  }
  .ingredient-name {
    padding-left: 10px;
    font-family: "Rye", serif;
    font-size: 34px;
    color: var(--ink);
    line-height: 1;
    white-space: nowrap;
  }
  .claim-band {
    position: absolute;
    left: 38px; top: 600px;
    width: 394px; height: 76px;
  }
  .claim-band svg { position: absolute; inset: 0; }
  .claim-title {
    position: absolute; left: 0; right: 0; top: 6px;
    text-align: center; color: var(--label);
    font-size: 27px; font-weight: 400; letter-spacing: 0.3px;
  }
  .claim-line {
    position: absolute; left: 0; right: 0; top: 48px;
    text-align: center; color: var(--label);
    font-size: 11px; font-weight: 300; letter-spacing: 0.2px;
  }
  .footer-row {
    position: absolute;
    left: 30px; right: 30px; top: 690px;
    height: 56px;
    display: flex; align-items: center; justify-content: space-between;
  }
  .seal {
    width: 54px; height: 54px; border-radius: 50%;
    border: 2px solid var(--tan);
  }
  .website {
    font-size: 17px; color: var(--ink); letter-spacing: 0.3px;
  }
</style>
</head>
<body>
  <div class="brand-name">TRAILHOP</div>

  <section class="front-label">
    <div class="hero-art" role="img" aria-label="Line illustration of a sheepdog's head in tan"></div>

    <ul class="ingredient-list">
      <li><span class="tick"><svg width="22" height="20" viewBox="0 0 22 20"><path d="M3 11 L8 17 L19 3" fill="none" stroke="#d6a06d" stroke-width="2.5" stroke-linecap="round" stroke-linejoin="round"/></svg></span><span class="ingredient-name">PEANUT BUTTER</span></li>
      <li><span class="tick"><svg width="22" height="20" viewBox="0 0 22 20"><path d="M3 11 L8 17 L19 3" fill="none" stroke="#d6a06d" stroke-width="2.5" stroke-linecap="round" stroke-linejoin="round"/></svg></span><span class="ingredient-name">SWEET POTATOES</span></li>
      <li><span class="tick"><svg width="22" height="20" viewBox="0 0 22 20"><path d="M3 11 L8 17 L19 3" fill="none" stroke="#d6a06d" stroke-width="2.5" stroke-linecap="round" stroke-linejoin="round"/></svg></span><span class="ingredient-name">POTATO FLOUR</span></li>
      <li><span class="tick"><svg width="22" height="20" viewBox="0 0 22 20"><path d="M3 11 L8 17 L19 3" fill="none" stroke="#d6a06d" stroke-width="2.5" stroke-linecap="round" stroke-linejoin="round"/></svg></span><span class="ingredient-name">FLAXSEED OIL</span></li>
      <li><span class="tick"><svg width="22" height="20" viewBox="0 0 22 20"><path d="M3 11 L8 17 L19 3" fill="none" stroke="#d6a06d" stroke-width="2.5" stroke-linecap="round" stroke-linejoin="round"/></svg></span><span class="ingredient-name">EGGS</span></li>
    </ul>

    <div class="claim-band">
      <svg width="394" height="76" viewBox="0 0 394 76" aria-hidden="true">
        <path d="M2 4 L390 0 L386 12 L392 24 L387 40 L393 52 L388 66 L372 74 L250 70 L120 76 L12 72 L4 60 L8 44 L1 30 L6 16 Z" fill="#6a2c15"/>
      </svg>
      <div class="claim-title">ALL-NATURAL, GRAIN-FREE</div>
      <div class="claim-line">FOR RESPONSIBLE DOG OWNERS THAT APPRECIATE QUALITY FOOD FOR THEIR PETS</div>
    </div>

    <div class="footer-row">
      <div class="seal"></div>
      <div class="website">WWW.TRAILHOPDEMO.NET</div>
      <div class="seal"></div>
    </div>
  </section>
</body>
</html>
```